NEW Modern Sleek Business Card for VR Language Startup

Our startup is using VR to lead the next wave of world language education. We need a two-sided business card that introduces the larger organization (Quorvel Language Inc) and our contact info on one side and shows the product, Lumidrasca, on the other side.

Side 1 (contact info)= Quorvel Logo and Contact info (name, title, phone, email)

Side 2 (product)= Lumidrasc logo, text, and website
Text= Culturally Immersive Language Learning Games
Website= www.lumidrasc.example

Target Market(s)

Education, Technology

Contact Information for Business Card

Contact info will be updated upon approval of the design. For now, put this as a placeholder.

Perry Hollins
Founder & CEO
phollins@mailtrove.example
(555)-014-2736

Font styles to use
Other font styles liked:
• Gibson and Century Gothic are the brand fonts

Requirements
Nice to have
• I would love to see cohesion between the design and colors of the two logos. I have attached a few business card designs that I like, so you can get a feel for my preferred style.

```html
<!DOCTYPE html>
<html lang="en">
<head>
<meta charset="UTF-8">
<title>Quorvel Language – Business Card</title>
<link rel="stylesheet" href="https://fonts.googleapis.com/css2?family=Montserrat:wght@500;700&family=Questrial&display=swap">
<style>
  :root {
    --stage: #1d1e22;
    --card-light: #4fb8ea;
    --card-mid: #1f7fcf;
    --card-deep: #0d3f96;
    --ink: #ffffff;
    --ink-soft: rgba(255,255,255,0.8);
    --mark: #f0504a;
  }
  * { margin: 0; padding: 0; box-sizing: border-box; }
  html, body { width: 1200px; height: 900px; overflow: hidden; }
  body {
    background: var(--stage);
    font-family: "Questrial", "Century Gothic", sans-serif;
    color: var(--ink);
    position: relative;
  }
  .card {
    position: absolute;
    width: 540px;
    height: 308px;
    border-radius: 26px;
    overflow: hidden;
    box-shadow: 0 18px 40px rgba(0,0,0,0.45);
  }
  .card-product { left: 40px; top: 296px; }
  .card-contact { left: 620px; top: 296px; }
  .card-backdrop { position: absolute; inset: 0; }
  .card-product .card-backdrop {
    background: radial-gradient(ellipse at 62% 40%, var(--card-light) 0%, var(--card-mid) 45%, var(--card-deep) 100%);
  }
  .card-contact .card-backdrop {
    background:
      radial-gradient(ellipse at 85% 85%, rgba(13,63,150,0.9) 0%, rgba(13,63,150,0) 60%),
      linear-gradient(160deg, var(--card-light) 0%, var(--card-mid) 55%, var(--card-deep) 100%);
  }
  .brand {
    position: absolute;
    display: flex;
    align-items: center;
    gap: 12px;
    white-space: nowrap;
  }
  .brand-dot {
    border-radius: 50%;
    background: var(--mark);
    flex: none;
  }
  .brand-name {
    font-family: "Montserrat", "Century Gothic", sans-serif;
    font-weight: 700;
    text-transform: uppercase;
    line-height: 1;
  }
  .card-product .brand { left: 190px; top: 118px; }
  .card-product .brand-dot { width: 36px; height: 36px; }
  .card-product .brand-name { font-size: 28px; letter-spacing: 4px; }

  .card-contact .brand { right: 34px; top: 214px; }
  .card-contact .brand-dot { width: 26px; height: 26px; }
  .card-contact .brand-name { font-size: 18px; letter-spacing: 3px; }

  .product-info {
    position: absolute; left: 34px; bottom: 32px;
    font-family: "Montserrat", sans-serif;
    font-weight: 500;
  }
  .product-site { font-size: 14px; margin-bottom: 6px; }
  .product-tagline { font-size: 15px; }

  .person { position: absolute; left: 36px; top: 34px; }
  .person-name {
    font-family: "Montserrat", sans-serif;
    font-weight: 700; font-size: 22px; letter-spacing: 2px;
    text-transform: uppercase;
  }
  .person-title { font-size: 13px; color: var(--ink-soft); margin-top: 4px; }
  .contact-list {
    position: absolute; left: 36px; top: 112px;
    list-style: none; font-size: 13px; color: var(--ink-soft);
  }
  .contact-list li { display: flex; align-items: center; gap: 10px; margin-bottom: 9px; white-space: nowrap; }
  .contact-icon { width: 12px; height: 12px; flex: none; }
</style>
</head>
<body>

<section class="card card-product">
  <div class="card-backdrop" role="img" aria-label="Blue gradient with a constellation network of lines and glowing dots"></div>
  <div class="brand">
    <span class="brand-dot"></span>
    <span class="brand-name">Lumidrasc</span>
  </div>
  <div class="product-info">
    <p class="product-site">www.lumidrasc.example</p>
    <p class="product-tagline">Culturally Immersive Language Learning Games</p>
  </div>
</section>

<section class="card card-contact">
  <div class="card-backdrop" role="img" aria-label="Blue gradient with a constellation network of lines and glowing dots in the lower right"></div>
  <div class="person">
    <p class="person-name">Perry Hollins</p>
    <p class="person-title">Founder &amp; CEO</p>
  </div>
  <ul class="contact-list">
    <li>
      <svg class="contact-icon" viewBox="0 0 12 12"><path d="M2 1h3l1 3-1.5 1a6 6 0 0 0 2.5 2.5L8 6l3 1v3a1 1 0 0 1-1 1A9 9 0 0 1 1 2a1 1 0 0 1 1-1z" fill="#fff"/></svg>
      (555)-014-2736
    </li>
    <li>
      <svg class="contact-icon" viewBox="0 0 12 12"><rect x="0.5" y="2" width="11" height="8" rx="1" fill="#fff"/><path d="M1 2.5l5 4 5-4" stroke="#1f7fcf" fill="none"/></svg>
      phollins@mailtrove.example
    </li>
    <li>
      <svg class="contact-icon" viewBox="0 0 12 12"><circle cx="6" cy="6" r="5.2" fill="none" stroke="#fff" stroke-width="1.2"/><path d="M0.8 6h10.4M6 0.8c-2.5 3-2.5 7.4 0 10.4M6 0.8c2.5 3 2.5 7.4 0 10.4" stroke="#fff" fill="none" stroke-width="0.9"/></svg>
      www.lumidrasc.example
    </li>
  </ul>
  <div class="brand">
    <span class="brand-dot"></span>
    <span class="brand-name">Quorvel Language</span>
  </div>
</section>

</body>
</html>
```